Business Card design for new private practice opening

I need a business card design for my new private practice with my new logo uploaded as a file
On the front the logo
On the back: maybe a small logo somewhere?
Priv. Doz. DDr. Corinna Vestaluk
Fachärztin für Allgemein- & Viszeralchirurgie
Address: xxx
Tel: xxx
Mobil:xxx
Webseite:xxx
Email:xxx

Contact Information for Business Card

See project description above for details

Requirements
Nice to have
• I would like the colors of the logo incorporated into the business card

```html
<!DOCTYPE html>
<html lang="de">
<head>
<meta charset="utf-8">
<title>Vestaluk Chirurgie – Visitenkarte</title>
<link rel="stylesheet" href="https://fonts.googleapis.com/css2?family=Poppins:wght@400;600&family=Montserrat:wght@600&display=swap">
<style>
  :root {
    --backdrop: #d6d6d6;
    --teal: #48b9b7;
    --white: #ffffff;
    --charcoal: #2e2e2e;
    --stone: #8a8a8a;
  }
  * { margin: 0; padding: 0; box-sizing: border-box; }
  html, body { width: 1093px; height: 1200px; overflow: hidden; }
  body {
    position: relative;
    background: var(--backdrop);
    font-family: "Poppins", sans-serif;
  }
  .card {
    position: absolute;
    left: 264px;
    width: 578px;
    height: 356px;
    border-radius: 27px;
    overflow: hidden;
  }
  .card--front { top: 226px; background: var(--teal); color: var(--white); }
  .card--back { top: 621px; background: var(--charcoal); }

  .front-art {
    position: absolute;
    left: 0;
    top: 21px;
    width: 216px;
    height: 335px;
  }

  .details {
    position: absolute;
    right: 31px;
    top: 44px;
    text-align: right;
  }
  .details__name {
    font-weight: 600;
    font-size: 16.5px;
    line-height: 22px;
    letter-spacing: 0.1px;
  }
  .details__title {
    font-weight: 400;
    font-size: 15.5px;
    line-height: 20px;
    margin-top: 1px;
  }
  .divider {
    width: 51px;
    height: 1px;
    background: var(--white);
    margin-left: auto;
    margin-top: 12px;
    margin-bottom: 10px;
  }
  .contact-list { list-style: none; margin-right: -4px; }
  .contact-list li {
    display: flex;
    justify-content: flex-end;
    align-items: center;
    gap: 5px;
    font-size: 16px;
    line-height: 23px;
  }
  .contact-list svg { width: 19px; height: 19px; flex: none; }
  .divider--lower { margin-top: 15px; margin-bottom: 12px; }
  .address { font-style: normal; font-size: 16px; line-height: 20px; }

  .brand {
    position: absolute;
    left: 48px;
    top: 105px;
    display: flex;
    align-items: center;
    gap: 20px;
  }
  .brand__disc {
    width: 146px;
    height: 146px;
    border-radius: 50%;
    background: var(--teal);
    flex: none;
  }
  .brand__name {
    font-family: "Montserrat", sans-serif;
    font-weight: 600;
    font-size: 54px;
    line-height: 60px;
    color: var(--stone);
    letter-spacing: 0.5px;
  }
</style>
</head>
<body>

<section class="card card--front">
  <svg class="front-art" viewBox="0 0 216 335" role="img" aria-label="Decorative brand artwork area">
    <path d="M0 335 V90 C60 80 90 40 120 20 C150 0 190 0 205 40 C216 80 216 200 200 270 C185 320 150 335 120 335 Z" fill="var(--white)"/>
  </svg>

  <div class="details">
    <p class="details__name">PRIV. DOZ. DDR. CORINNA VESTALUK</p>
    <p class="details__title">Fachärztin für Allgemein- &amp;<br>Viszeralchirurgie</p>
    <div class="divider"></div>
    <ul class="contact-list">
      <li>044-123 456 789
        <svg viewBox="0 0 20 20" aria-hidden="true"><circle cx="10" cy="10" r="9" fill="none" stroke="currentColor" stroke-width="1.2"/><path d="M6.5 6 l2 -0.5 l1 2.2 l-1.2 1 a6 6 0 0 0 3 3 l1 -1.2 l2.2 1 l-0.5 2 c-4 0 -7.5 -3.5 -7.5 -7.5z" fill="currentColor"/></svg>
      </li>
      <li>044-123 456 789
        <svg viewBox="0 0 20 20" aria-hidden="true"><circle cx="10" cy="10" r="9" fill="none" stroke="currentColor" stroke-width="1.2"/><rect x="7" y="5" width="6" height="10" rx="1" fill="none" stroke="currentColor" stroke-width="1.2"/><circle cx="10" cy="13" r="0.7" fill="currentColor"/></svg>
      </li>
      <li>info@webname.com
        <svg viewBox="0 0 20 20" aria-hidden="true"><circle cx="10" cy="10" r="9" fill="none" stroke="currentColor" stroke-width="1.2"/><rect x="5.5" y="7" width="9" height="6.5" fill="currentColor"/><path d="M5.5 7 l4.5 3.5 l4.5 -3.5" fill="none" stroke="var(--teal)" stroke-width="0.9"/></svg>
      </li>
      <li>www.websitename.com
        <svg viewBox="0 0 20 20" aria-hidden="true"><circle cx="10" cy="10" r="9" fill="none" stroke="currentColor" stroke-width="1.2"/><circle cx="10" cy="10" r="5" fill="none" stroke="currentColor" stroke-width="1"/><ellipse cx="10" cy="10" rx="2.2" ry="5" fill="none" stroke="currentColor" stroke-width="1"/><path d="M5 10 h10 M5.8 7.5 h8.4 M5.8 12.5 h8.4" stroke="currentColor" stroke-width="0.8"/></svg>
      </li>
    </ul>
    <div class="divider divider--lower"></div>
    <address class="address">421, Address line goes here<br>45452,Country Name</address>
  </div>
</section>

<section class="card card--back">
  <div class="brand">
    <div class="brand__disc"></div>
    <p class="brand__name">VESTALUK<br>CHIRURGIE</p>
  </div>
</section>

</body>
</html>
```